DL Flyer announcing opening of Thistle Fern Row Homewares & Gift Store

To create 2 sided full colour DL Flyer which will be distributed by a letterbox drop to announce the opening of a delightful new homewares and gift store called "Thistle Fern Row Homewares" at 87 Marlowe Creek Road, Northbridge.

Thistle Fern Row Homewares offers a range of exclusive, bespoke, well-crafted decorative homewares and gifts. Our target market is well to do and aspirational, so we want the design of the flyer to match.

The owners, Brenda (a long-time resident of Northbridge) and Lorna have combined their love of homewares and years of retail experience to create this fresh and exciting new store.

Thistle Fern Row will cater for all those special occasions throughout the year but right now as we move into Christmas we have some beautiful Christmas decorations. Why not come in and visit Lorna who has 18 years experience in the Christmas industry and find out about our Christmas Tree decorating service.

Also we want a call to action so want to offer a 10% discount for people who bring the flyer in during the month of November

The store is open Tuesday to Friday 9.30am to 5.00pm and Saturday 10.00am to 4.00pm

Please find attached duck design we are using the coloured version (excluding the word 'duck' of course). The colour we have chosen for Thistle Fern Row is "Duck Egg Blue" and the font is Lucida Calligraphy.

Thank you

Target Market(s)

is well to do and aspirational

Industry/Entity Type

Store

• Lucida Calligraphy

Colors
cfeae6

Requirements
Must have
• the Duck. Discount voucher, address, look forward to being of service for many years to come. "Duck Egg Blue" colour tones

```html
<!DOCTYPE html>
<html lang="en">
<head>
<meta charset="utf-8">
<title>Thistle Fern Row Homewares – DL Flyer</title>
<link rel="stylesheet" href="https://fonts.googleapis.com/css2?family=Arimo&family=Fjalla+One&family=Montserrat:wght@600&family=Open+Sans:ital,wght@0,400;0,600;0,700;1,400&family=Yanone+Kaffeesatz:wght@400&family=Zilla+Slab:wght@400&family=Encode+Sans+Condensed:wght@400&display=swap">
<style>
  :root {
    --page: #e7e2d8;
    --card-front: #f1eee4;
    --card-back: #f3ebda;
    --duck-egg: #cfeae6;
    --teal: #5cbfb7;
    --teal-deep: #1e4f57;
    --rose: #f2848a;
    --ribbon: #a9c1ca;
    --ink: #222222;
    --xmas-red: #d6292e;
    --xmas-red-text: #e2262b;
    --pine: #1f5a2a;
    --parchment: #fbf2cd;
    --white: #ffffff;
  }
  * { box-sizing: border-box; margin: 0; padding: 0; }
  html, body { width: 1200px; height: 1200px; overflow: hidden; }
  body { background: var(--page); position: relative; font-family: "Open Sans", sans-serif; color: var(--ink); }

  .flyer { position: absolute; left: 50px; width: 1093px; height: 520px; overflow: hidden; }
  .flyer--front { top: 53px; background: var(--card-front); }
  .flyer--back { top: 618px; background: var(--card-back); }
  .abs { position: absolute; }
  .center { text-align: center; }

  /* brand mark */
  .brand-mark { position: absolute; border-radius: 50%; background: var(--duck-egg); border: 4px solid var(--white); box-shadow: 0 0 0 2px var(--duck-egg); display: flex; align-items: center; justify-content: center; text-align: center; font-family: "Zilla Slab", serif; color: var(--teal-deep); }

  /* front */
  .intro { left: 0; width: 1093px; top: 20px; font-family: "Montserrat", sans-serif; font-weight: 600; font-size: 22px; letter-spacing: 1.2px; }
  .headline { left: 341px; width: 400px; top: 56px; font-family: "Arimo", sans-serif; font-size: 80px; line-height: 68px; color: var(--rose); letter-spacing: -1px; }
  .voucher { left: 348px; top: 277px; width: 396px; height: 158px; }
  .voucher-text { left: 348px; width: 396px; font-style: italic; }
  .voucher-lead { top: 296px; font-size: 26px; color: #333; }
  .voucher-offer { top: 322px; font-style: normal; font-weight: 700; font-size: 56px; color: var(--white); }
  .voucher-note { top: 387px; font-size: 19px; color: #333; }
  .address { left: 341px; width: 400px; top: 443px; font-weight: 600; font-size: 25px; line-height: 30px; }
  .range { left: 800px; width: 270px; top: 118px; font-family: "Zilla Slab", serif; font-size: 24px; line-height: 26px; color: var(--teal); }
  .hours { left: 822px; top: 247px; width: 225px; height: 155px; background: var(--teal-deep); border: 3px solid var(--white); box-shadow: 0 0 0 1px #c9d6d6; color: var(--white); font-size: 18.5px; line-height: 27px; padding-top: 9px; }
  .hours-title { font-weight: 700; font-style: italic; }
  .hours strong { font-weight: 700; }

  /* back */
  .tree-art { left: 0; top: 0; width: 300px; height: 520px; background: linear-gradient(100deg, var(--pine) 0%, #2d7a35 55%, rgba(45,122,53,0) 100%); }
  .collection-band { left: 100px; top: 32px; width: 440px; height: 155px; }
  .collection-text { left: 134px; top: 48px; font-family: "Yanone Kaffeesatz", sans-serif; font-size: 37px; line-height: 39px; color: var(--white); }
  .tree-badge { left: 447px; top: 32px; width: 160px; height: 160px; }
  .bauble { left: 625px; top: 32px; width: 76px; height: 76px; border-radius: 50%; background: radial-gradient(circle at 40% 35%, #ffffff, #dcdcdc); }
  .service-title { left: 640px; width: 455px; top: 30px; font-family: "Fjalla One", sans-serif; font-size: 36px; line-height: 45px; color: var(--xmas-red-text); }
  .service-sub { left: 680px; width: 380px; top: 129px; font-size: 22px; line-height: 26px; }
  .owners-frame { left: 655px; top: 196px; width: 400px; height: 200px; }
  .owners-text { left: 685px; width: 340px; top: 252px; font-family: "Encode Sans Condensed", sans-serif; font-size: 16.5px; line-height: 22.3px; color: #c8212a; }
  .occasions { left: 290px; top: 442px; width: 803px; height: 50px; background: var(--duck-egg); font-family: "Zilla Slab", serif; font-size: 24px; line-height: 50px; letter-spacing: 0.6px; color: var(--teal); padding-left: 22px; }
</style>
</head>
<body>

<section class="flyer flyer--front" aria-label="Flyer front">
  <div class="brand-mark" style="left:35px;top:117px;width:286px;height:286px;font-size:32px;line-height:38px;">Thistle Fern Row<br>Home Wares</div>

  <p class="abs intro center">We want the neighborhood to know that</p>
  <h1 class="abs headline center">WE OPEN<br>A NEW<br>STORE</h1>

  <svg class="abs voucher" viewBox="0 0 396 158" aria-hidden="true">
    <polygon points="0,10 396,0 380,79 396,158 0,148 16,79" fill="var(--ribbon)"/>
    <polygon points="0,10 396,0 380,79 396,158 0,148 16,79" fill="none" stroke="#fff" stroke-width="0" />
    <line x1="22" y1="18" x2="374" y2="9" stroke="#fff" stroke-width="1.5" stroke-dasharray="5 4"/>
    <line x1="22" y1="140" x2="374" y2="149" stroke="#fff" stroke-width="1.5" stroke-dasharray="5 4"/>
  </svg>
  <p class="abs voucher-text voucher-lead center">Present This Flyer and Get</p>
  <p class="abs voucher-text voucher-offer center">10% OFF</p>
  <p class="abs voucher-text voucher-note center">During the month of November</p>

  <p class="abs address center">87 Marlowe Creek Road,<br>Northbridge</p>

  <p class="abs range center">Check out our range of exclusive, bespoke, well-crafted decorative homewares and gifts.</p>

  <div class="abs hours center">
    <p class="hours-title">STORE HOURS:</p>
    <p>Tuesday to Friday</p>
    <p><strong>9:30 AM to 5:00 PM</strong></p>
    <p>Saturday</p>
    <p><strong>10:00 AM to 4:00 PM</strong></p>
  </div>
</section>

<section class="flyer flyer--back" aria-label="Flyer back">
  <div class="abs tree-art" role="img" aria-label="Decorated Christmas tree branches with baubles and candy canes"></div>

  <svg class="abs collection-band" viewBox="0 0 440 155" aria-hidden="true">
    <rect x="0" y="0" width="440" height="155" fill="var(--xmas-red)"/>
    <line x1="14" y1="12" x2="430" y2="12" stroke="#fff" stroke-width="3" stroke-linecap="round" stroke-dasharray="0 11"/>
    <line x1="14" y1="143" x2="430" y2="143" stroke="#fff" stroke-width="3" stroke-linecap="round" stroke-dasharray="0 11"/>
  </svg>
  <p class="abs collection-text">Check out our Collection<br>of beautiful Christmas<br>ornaments &amp; decorations</p>

  <div class="abs tree-badge" role="img" aria-label="Red diamond badge with a Christmas tree icon">
    <svg viewBox="0 0 160 160" width="160" height="160" aria-hidden="true">
      <polygon points="80,0 160,80 80,160 0,80" fill="#c91f27"/>
    </svg>
  </div>

  <div class="abs bauble" role="img" aria-label="White patterned Christmas bauble"></div>

  <h2 class="abs service-title center">We offer Christmas Tree<br>Decorating Service</h2>
  <p class="abs service-sub center">With18 years experience<br>in the Christmas industry.</p>

  <svg class="abs owners-frame" viewBox="0 0 400 200" aria-hidden="true">
    <polygon points="40,30 360,30 395,100 360,180 40,180 5,100" fill="var(--parchment)" stroke="#d6292e" stroke-width="1.5"/>
    <polygon points="48,38 352,38 385,100 352,172 48,172 15,100" fill="none" stroke="#d6292e" stroke-width="1"/>
  </svg>
  <p class="abs owners-text center">Thistle Fern Row Home Wares is owned and operated by Brenda (a long-time resident of Northbridge) and Lorna who have combined their love of homewares and years of retail experience to create this fresh and exciting new store.</p>

  <div class="brand-mark" style="left:310px;top:214px;width:200px;height:200px;font-size:24px;line-height:28px;">Thistle Fern Row<br>Home Wares</div>

  <p class="abs occasions">We will cater for all those special occasions throughout the year.</p>
</section>

</body>
</html>
```